Speisekarte für eine Strand-Pizzeria in Kroatien gesucht
Zielgruppe
Eine Pizzeria in einer sehr kleinen Siedlung am Meer in Kroatien, die mehr als nur Pizza anbietet. Zielgruppe sind Touristen und Ferienwohnungs-Besitzer. Die Pizzeria bietet viele verschiedene lokale und internationale Gerichte.
Aufgabenstellung
Bedient wird hauptsächlich draußen auf der Terrasse, so dass die Karten in sehr heller Umgebung im Sommer benutzt werden. Die Karte soll nicht kleiner sein als A5, aber auch nicht größer als A4.
Der Print wird später entweder laminiert oder in einer anderen langliebegen Form sein, damit die Karten mehr als 2 Saisons aushalten.
Die meisten Gerichte sollen in einer sehr schönen Form durch ein Foto dargestellt werden und intelligent angeordnet werden. Einladende Fotos brauchen wir natürlich auch (z.B. Bildarko o.ä). Bei Pizza könnte man eine Ausnahme machen und nicht jede Pizza darstellen, sondern vielleicht eine oder 2 Arten etwas größer darstellen. Eine Karte die wir sehr schön finden sind die von Teig-Kiste, vielleicht kann man sich hier anlehnen.
Die erste Seite bei zugeklappter Karte ist am wichtigsten und soll zum Essen einladen.
Das Logo ist fix (2 Palmen), aber der Schriftzug des Lokals (MELUVERA) steht noch nicht. Hier könnten wir auch eine eigene Schrift gebrauchen, die wiedererkennbar ist, da es 2 Locations gibt.
Die Karte muss in 5 Sprachen verständlich sein (siehe Fotos).
UPDATE: Sollten SIE als Designer nicht alle 5 Sprachen kennen, übernehmen Sie den Text der alten Karte (trotz Fehler). Diese Fehler können wir dann, nach Auswahl des finalen Designs verbessern.
Die aktuelle und katastrophale Karte ist angehängt (bitte beachten, dass hier sehr viele Schreibfehler sind).
UPDATE: Alle Gerichte die auf der alten Karte im Anhang angezeigt werden, sollen in Zukunft auch serviert werden.

```html
<!DOCTYPE html>
<html lang="de">
<head>
<meta charset="utf-8">
<title>MELUVERA Speisekarte</title>
<link rel="stylesheet" href="https://fonts.googleapis.com/css2?family=Questrial&family=Yanone+Kaffeesatz:wght@300;400&display=swap">
<style>
  :root {
    --backdrop: #cdac8c;
    --paper: #ffffff;
    --paper-shade: #ececec;
    --brown: #7a3f0c;
    --brown-text: #7a3f0c;
    --ink: #333333;
    --rule: #8a8a8a;
    --white: #ffffff;
    --accent-red: #d8321e;
  }
  * { box-sizing: border-box; margin: 0; padding: 0; }
  html, body { width: 1200px; height: 900px; overflow: hidden; }
  body {
    background: var(--backdrop);
    font-family: "Questrial", "Century Gothic", sans-serif;
    display: flex;
    align-items: center;
    justify-content: center;
  }
  .menu-spread {
    display: flex;
    width: 580px;
    height: 860px;
    box-shadow: 0 10px 30px rgba(0,0,0,.18);
  }

  /* Pizza panel */
  .panel-pizza {
    width: 290px;
    height: 100%;
    background: linear-gradient(to bottom, var(--paper) 0%, var(--paper) 70%, var(--paper-shade) 100%);
    padding: 20px 20px 14px 22px;
    display: flex;
    flex-direction: column;
  }
  .brand {
    display: flex;
    align-items: center;
    justify-content: flex-end;
    gap: 6px;
  }
  .brand-mark {
    width: 26px; height: 26px;
    border-radius: 50%;
    background: var(--accent-red);
  }
  .brand-name {
    font-size: 9px;
    letter-spacing: .5px;
    color: var(--ink);
  }
  .section-title {
    font-size: 24px;
    font-weight: 400;
    color: var(--ink);
    letter-spacing: 1px;
    padding: 10px 0 6px;
    border-bottom: 1px solid var(--rule);
  }
  .item-group {
    padding: 18px 0 20px;
    border-bottom: 1px solid var(--rule);
  }
  .item {
    display: flex;
    align-items: baseline;
    font-size: 13px;
    line-height: 15px;
    color: var(--brown-text);
  }
  .item-name { white-space: nowrap; }
  .item-leader {
    flex: 1;
    border-bottom: 1px dotted currentColor;
    margin: 0 1px 3px;
  }
  .item-price { white-space: nowrap; }
  .feature-photo {
    margin-top: auto;
    height: 150px;
    border-radius: 50%;
    background: radial-gradient(ellipse at 50% 60%, #5a2a14 0%, #8a4a22 30%, #e08a3a 55%, #f6f1ea 75%, #ececec 100%);
  }
  .photo-code {
    font-size: 6px;
    color: var(--ink);
    text-align: right;
    margin-top: 6px;
  }

  /* Other dishes panel */
  .panel-sonstiges {
    width: 290px;
    height: 100%;
    background: var(--brown);
    padding: 24px 14px 20px 14px;
    color: var(--white);
    display: flex;
    flex-direction: column;
  }
  .panel-sonstiges .section-title {
    font-family: "Yanone Kaffeesatz", "Arial Narrow", sans-serif;
    font-weight: 300;
    font-size: 26px;
    letter-spacing: 0;
    color: var(--white);
    border: 0;
    padding: 0 0 10px 8px;
  }
  .dish {
    margin-bottom: 14px;
  }
  .dish-photo {
    height: 118px;
    margin-bottom: 8px;
  }
  .photo-veg-glasses { background: linear-gradient(135deg, #9fd07a, #5e9a3a 50%, #e2b08a); }
  .photo-fish { background: linear-gradient(135deg, #c99a5a, #7d6450 50%, #e0b04a); }
  .photo-salad { background: linear-gradient(135deg, #e6ece0, #5f9a3c 50%, #e06a52); }
  .photo-bowl { background: linear-gradient(135deg, #3f6a3a, #d9c04a 50%, #556c7a); }
  .dish .item {
    font-family: "Yanone Kaffeesatz", "Arial Narrow", sans-serif;
    font-weight: 300;
    font-size: 15px;
    line-height: 19px;
    color: var(--white);
    padding: 0 4px;
  }
</style>
</head>
<body>
  <main class="menu-spread">
    <section class="panel-pizza">
      <header class="brand">
        <span class="brand-mark"></span>
        <span class="brand-name">MELUVERA</span>
      </header>
      <h2 class="section-title">PIZZA</h2>

      <div class="item-group">
        <p class="item"><span class="item-name">Spezial Salat</span><span class="item-leader"></span><span class="item-price">5€</span></p>
        <p class="item"><span class="item-name">Spezial Salat</span><span class="item-leader"></span><span class="item-price">5€</span></p>
        <p class="item"><span class="item-name">Spezial Salat</span><span class="item-leader"></span><span class="item-price">5€</span></p>
      </div>
      <div class="item-group">
        <p class="item"><span class="item-name">Spezial Salat</span><span class="item-leader"></span><span class="item-price">5€</span></p>
        <p class="item"><span class="item-name">Spezial Salat</span><span class="item-leader"></span><span class="item-price">5€</span></p>
        <p class="item"><span class="item-name">Spezial Salat</span><span class="item-leader"></span><span class="item-price">5€</span></p>
      </div>
      <div class="item-group">
        <p class="item"><span class="item-name">Spezial Salat</span><span class="item-leader"></span><span class="item-price">5€</span></p>
        <p class="item"><span class="item-name">Spezial Salat</span><span class="item-leader"></span><span class="item-price">5€</span></p>
        <p class="item"><span class="item-name">Spezial Salat</span><span class="item-leader"></span><span class="item-price">5€</span></p>
      </div>
      <div class="item-group">
        <p class="item"><span class="item-name">Spezial Salat</span><span class="item-leader"></span><span class="item-price">5€</span></p>
        <p class="item"><span class="item-name">Spezial Salat</span><span class="item-leader"></span><span class="item-price">5€</span></p>
        <p class="item"><span class="item-name">Spezial Salat</span><span class="item-leader"></span><span class="item-price">5€</span></p>
      </div>
      <div class="item-group">
        <p class="item"><span class="item-name">Spezial Salat</span><span class="item-leader"></span><span class="item-price">5€</span></p>
        <p class="item"><span class="item-name">Spezial Salat</span><span class="item-leader"></span><span class="item-price">5€</span></p>
        <p class="item"><span class="item-name">Spezial Salat</span><span class="item-leader"></span><span class="item-price">5€</span></p>
      </div>
      <div class="item-group">
        <p class="item"><span class="item-name">Spezial Salat</span><span class="item-leader"></span><span class="item-price">5€</span></p>
        <p class="item"><span class="item-name">Spezial Salat</span><span class="item-leader"></span><span class="item-price">5€</span></p>
        <p class="item"><span class="item-name">Spezial Salat</span><span class="item-leader"></span><span class="item-price">5€</span></p>
      </div>

      <div class="feature-photo" role="img" aria-label="Foto: gegrillte Steaks mit Karotten, Ofenkartoffeln und Salat auf weißem Teller"></div>
      <p class="photo-code">#204857316</p>
    </section>

    <section class="panel-sonstiges">
      <h2 class="section-title">Sonstiges</h2>

      <article class="dish">
        <div class="dish-photo photo-veg-glasses" role="img" aria-label="Foto: Gemüsesticks mit Kräuterdip in Gläsern"></div>
        <p class="item"><span class="item-name">Spezial Salat</span><span class="item-leader"></span><span class="item-price">5€</span></p>
        <p class="item"><span class="item-name">Spezial Salat</span><span class="item-leader"></span><span class="item-price">5€</span></p>
      </article>
      <article class="dish">
        <div class="dish-photo photo-fish" role="img" aria-label="Foto: gegrillte Forelle mit Zitrone und Dill auf Backpapier"></div>
        <p class="item"><span class="item-name">Spezial Salat</span><span class="item-leader"></span><span class="item-price">5€</span></p>
        <p class="item"><span class="item-name">Spezial Salat</span><span class="item-leader"></span><span class="item-price">5€</span></p>
      </article>
      <article class="dish">
        <div class="dish-photo photo-salad" role="img" aria-label="Foto: Rucolasalat mit Spargel und Erdbeeren"></div>
        <p class="item"><span class="item-name">Spezial Salat</span><span class="item-leader"></span><span class="item-price">5€</span></p>
        <p class="item"><span class="item-name">Spezial Salat</span><span class="item-leader"></span><span class="item-price">5€</span></p>
      </article>
      <article class="dish">
        <div class="dish-photo photo-bowl" role="img" aria-label="Foto: Schüssel mit Quinoa-Bohnen-Mais-Salat"></div>
        <p class="item"><span class="item-name">Spezial Salat</span><span class="item-leader"></span><span class="item-price">5€</span></p>
        <p class="item"><span class="item-name">Spezial Salat</span><span class="item-leader"></span><span class="item-price">5€</span></p>
      </article>
    </section>
  </main>
</body>
</html>
```